Foot doctor needs feet friendly business cards.

Business cards for Podiatrist. Needs to look professional and modern. Back side put an appointment card, and try to put a little basic street map somewhere on card along with all of our contact info below:

Marcus Hollend, DPM, Inc.
Diplomate, National Council of Lower Limb Practice
Call: 1.877.Walk.482
1.555.238.6149
Fax: 1.555.871.3902
Email: info@DrHollend.example
Web: www.DrHollend.example
2741 N. Harbor Ln. Suite 208
Costa Mesa, CA 90413

```html
<!DOCTYPE html>
<html lang="en">
<head>
<meta charset="utf-8">
<title>Marcus Hollend, DPM, Inc. — Business &amp; Appointment Cards</title>
<link rel="stylesheet" href="https://fonts.googleapis.com/css2?family=Source+Sans+3:wght@300;400;600;700&display=swap">
<style>
  :root {
    --bg: #2b2b2d;
    --card-dark: #2a1f1d;
    --card-dark-soft: #3a2c29;
    --paper: #ffffff;
    --ink: #231815;
    --muted: #8a8a8a;
    --grey-band: #a6a6a8;
    --line: #d9d2cf;
    --light-text: #f2eeec;
  }
  * { margin: 0; padding: 0; box-sizing: border-box; }
  html, body { width: 1200px; height: 900px; overflow: hidden; }
  body {
    background: var(--bg);
    font-family: "Source Sans 3", Arial, sans-serif;
    position: relative;
  }
  .card {
    position: absolute;
    left: 290px;
    width: 620px;
    height: 354px;
    border-radius: 4px;
    overflow: hidden;
    box-shadow: 0 10px 30px rgba(0,0,0,.45);
  }

  /* Appointment side */
  .appointment-card { top: 70px; background: var(--card-dark); color: var(--light-text); }
  .appointment-card .brand {
    position: absolute; top: 26px; right: 30px;
    display: flex; align-items: center; gap: 8px;
  }
  .brand-dot { width: 12px; height: 12px; border-radius: 50%; background: var(--light-text); }
  .brand-text { font-size: 13px; font-weight: 600; line-height: 1.1; }
  .brand-text small { display: block; font-size: 8px; font-weight: 400; opacity: .8; }
  .appointment-title {
    position: absolute; top: 62px; left: 30px;
    font-size: 34px; font-weight: 700; letter-spacing: .5px;
  }
  .appointment-fields { position: absolute; top: 126px; left: 30px; right: 40px; }
  .field { display: flex; align-items: flex-end; height: 30px; }
  .field-label { width: 110px; font-size: 13px; }
  .field-line { flex: 1; border-bottom: 1px solid var(--line); height: 1px; margin-bottom: 4px; opacity: .8; }
  .appointment-note { position: absolute; top: 270px; left: 30px; font-size: 14.5px; }
  .appointment-call { position: absolute; top: 296px; left: 0; right: 0; text-align: center; font-size: 20px; font-weight: 600; letter-spacing: .5px; }

  /* Business side */
  .business-card { top: 470px; background: var(--paper); color: var(--ink); }
  .business-card .shapes { position: absolute; inset: 0; }
  .identity { position: absolute; top: 34px; left: 36px; display: flex; gap: 16px; align-items: flex-start; }
  .identity-dot { width: 48px; height: 48px; border-radius: 50%; background: var(--ink); margin-top: 6px; }
  .doctor-name { font-size: 36px; font-weight: 700; line-height: 1; letter-spacing: .2px; }
  .doctor-title { font-size: 15px; color: var(--muted); margin-top: 4px; letter-spacing: .3px; }
  .address { position: absolute; top: 120px; right: 34px; font-size: 15px; color: var(--muted); line-height: 1.3; font-weight: 300; }
  .contact-list { position: absolute; top: 166px; left: 36px; list-style: none; font-size: 15px; color: var(--muted); font-weight: 300; }
  .contact-list li { display: flex; align-items: center; gap: 10px; height: 22px; }
  .contact-list svg { width: 13px; height: 13px; fill: var(--ink); stroke: var(--ink); }
  .phones { position: absolute; top: 166px; left: 170px; font-size: 15px; color: var(--muted); font-weight: 300; }
</style>
</head>
<body>

<section class="card appointment-card" aria-label="Appointment card">
  <div class="brand">
    <span class="brand-dot"></span>
    <div class="brand-text">Marcus Hollend, DPM, Inc.<small>Diplomate, National Council of Lower Limb Practice</small></div>
  </div>
  <h1 class="appointment-title">Appointment</h1>
  <div class="appointment-fields">
    <div class="field"><span class="field-label">For</span><span class="field-line"></span></div>
    <div class="field"><span class="field-label">Date</span><span class="field-line"></span></div>
    <div class="field"><span class="field-label">Time</span><span class="field-line"></span></div>
    <div class="field"><span class="field-label">Location</span><span class="field-line"></span></div>
  </div>
  <p class="appointment-note">If you are unable to keep your appointment , please contact us as soon as possible</p>
  <p class="appointment-call">CALL : 877.925.4820</p>
</section>

<section class="card business-card" aria-label="Business card">
  <svg class="shapes" viewBox="0 0 620 354" preserveAspectRatio="none">
    <polygon points="0,300 330,300 360,262 620,262 620,354 0,354" fill="var(--card-dark)"/>
    <polygon points="420,262 620,244 620,262" fill="var(--grey-band)"/>
    <rect x="430" y="244" width="190" height="18" fill="var(--grey-band)"/>
  </svg>
  <div class="identity">
    <span class="identity-dot"></span>
    <div>
      <h2 class="doctor-name">Marcus Hollend, DPM, Inc.</h2>
      <p class="doctor-title">Diplomate, National Council of Lower Limb Practice</p>
    </div>
  </div>
  <address class="address">
    2741 N. Harbor Ln. Suite 208<br>Costa Mesa, CA 90413<br>
    <span>&#9635; 1.555.871.3902</span>
  </address>
  <ul class="contact-list">
    <li><svg viewBox="0 0 16 16"><path d="M3 1l3 3-2 2c1 2 3 4 5 5l2-2 3 3-2 3C6 14 2 10 1 3z" stroke="none"/></svg>1.877.Walk.482 / 1.555.238.6149</li>
    <li><svg viewBox="0 0 16 16"><circle cx="8" cy="8" r="6.5" fill="none" stroke-width="1.5"/><path d="M1.5 8h13M8 1.5c-3 3-3 10 0 13M8 1.5c3 3 3 10 0 13" fill="none" stroke-width="1.2"/></svg>www.DrHollend.example</li>
    <li><svg viewBox="0 0 16 16"><circle cx="8" cy="8" r="3" fill="none" stroke-width="2"/><path d="M11 5v4c0 2 3 2 3-1A6 6 0 1 0 11 13" fill="none" stroke-width="2"/></svg>info@DrHollend.example</li>
  </ul>
</section>

</body>
</html>
```